Commercial Construction Company

We need a business card design based on our current logo. We are a commercial general contractor based in Southern California that specializes in bank remodels. We would like to see designs that incorporate dark blue. The final design should portray an image of professionalism and quality.

If possible, I would like to add metallic foil to the design. Thank you

```html
<!DOCTYPE html>
<html lang="en">
<head>
<meta charset="utf-8">
<title>Harlow Commercial – Business Card</title>
<link href="https://fonts.googleapis.com/css2?family=Arimo:wght@400;700&display=swap" rel="stylesheet">
<style>
  :root{
    --sky-deep:#4a9fd8;
    --sky-light:#6ac8ec;
    --navy:#1d3f7a;
    --ink:#111418;
    --white:#ffffff;
    --page:#eef1f4;
  }
  *{box-sizing:border-box;margin:0;padding:0}
  html,body{width:1200px;height:900px;overflow:hidden;background:var(--page)}
  body{font-family:"Arimo",Arial,sans-serif;position:relative}
  .card{
    position:absolute;left:320px;width:560px;height:320px;border-radius:28px;overflow:hidden;
    box-shadow:0 6px 18px rgba(0,0,0,.15);
  }
  .card-back{top:50px;background:linear-gradient(160deg,var(--sky-deep) 40%,var(--sky-light) 100%)}
  .card-front{top:450px;background:linear-gradient(200deg,var(--sky-deep) 0%,var(--sky-light) 50%,var(--sky-deep) 100%)}
  .brand{display:flex;align-items:center;gap:12px;position:absolute}
  .brand-dot{width:22px;height:22px;border-radius:50%;background:var(--navy)}
  .brand-name{font-weight:700;color:var(--ink);letter-spacing:.5px}
  .card-back .brand{left:50%;top:50%;transform:translate(-50%,-50%)}
  .card-back .brand-name{font-size:34px}
  .logo-panel{
    position:absolute;left:250px;top:-30px;width:460px;height:460px;border-radius:50%;background:var(--white);
  }
  .card-front .brand{left:300px;top:180px}
  .card-front .brand-name{font-size:26px}
  .contact{position:absolute;left:34px;top:36px;color:var(--white)}
  .person{display:flex;align-items:flex-start;gap:10px}
  .person-name{font-size:24px;font-weight:700;color:var(--navy);letter-spacing:1px}
  .person-role{font-size:18px;color:var(--navy);margin-top:2px}
  .divider{width:200px;height:2px;background:var(--white);margin:10px 0 18px 30px}
  .lines{list-style:none}
  .lines li{display:flex;align-items:center;gap:10px;font-size:17px;margin-bottom:9px}
  .icon{width:22px;height:22px;flex:none}
</style>
</head>
<body>
  <section class="card card-back" aria-label="Card back">
    <div class="brand"><span class="brand-dot"></span><span class="brand-name">Harlow Commercial</span></div>
  </section>

  <section class="card card-front" aria-label="Card front">
    <div class="logo-panel"></div>
    <div class="brand"><span class="brand-dot"></span><span class="brand-name">Harlow Commercial</span></div>
    <div class="contact">
      <div class="person">
        <svg class="icon" viewBox="0 0 22 22"><circle cx="11" cy="11" r="11" fill="#111418"/><circle cx="11" cy="8" r="3.5" fill="#fff"/><path d="M5 17c1-4 11-4 12 0z" fill="#fff"/></svg>
        <div>
          <div class="person-name">Marcus Delaney</div>
          <div class="person-role">Founder&amp;CEO</div>
        </div>
      </div>
      <div class="divider"></div>
      <ul class="lines">
        <li><svg class="icon" viewBox="0 0 22 22"><circle cx="11" cy="11" r="11" fill="#111418"/><path d="M7 6c1-1 2 0 3 2s0 2-1 3c1 2 2 3 3 3 1-1 1-2 3-1s2 2 1 3c-3 2-10-4-9-10z" fill="#fff"/></svg>00-000-0000</li>
        <li><svg class="icon" viewBox="0 0 22 22"><circle cx="11" cy="11" r="11" fill="#111418"/><rect x="5" y="7" width="12" height="8" fill="#fff"/><path d="M5 7l6 5 6-5" stroke="#111418" fill="none"/></svg>info@yourdomain.com</li>
        <li><svg class="icon" viewBox="0 0 22 22"><circle cx="11" cy="11" r="11" fill="#111418"/><circle cx="11" cy="11" r="6" fill="none" stroke="#fff" stroke-width="1.5"/><path d="M5 11h12M11 5c-3 3-3 9 0 12M11 5c3 3 3 9 0 12" stroke="#fff" fill="none"/></svg>www.yourwebsite.com</li>
      </ul>
    </div>
  </section>
</body>
</html>
```